Postcard design for accounting company

We need a postcard design (front and back) to our accounting firm that provides bookkeeping services to small and mid-size companies using LedgerPad Online. We would like to see designs that use the color blue and match our overall branding (see website). The final design should communicate professionalism, trust, and ease.

Target Market(s)

Small and Mid-Size companies

Industry/Entity Type

Accounting

Colors
0054AA
0677BA
7BADD7
CADEEF
E8F1F8

Requirements
Must have
• Logo, contact information, indicate services offered, color blue, and fit postcard template (see attached). Contact info = 555.318.2207, 1.800.555.0142, Info@BrightLedgerAccounting.com, www.BrightLedgerAccounting.com. Use the ZRPX Retail Indicia, which is a postage payment mark that takes the place of a regular postage stamp or meter stamp. Every ZRPX mailpiece must include the ZRPX Retail Indicia above and to the right of the address block. The ZRPX Retail Indicia does not have a specific size requirement but must be larger than 0.5" x 0.5". The type font must be in all caps and at least a 4 point size. It should fit in the area 1.625" from the right edge and 1.375" from top edge. Leave 1/8" of space around the top and right edge. See attached sample.
Nice to have
• Include that we a re Certified LedgerPad CertPartners (can include LPO logo). Also, maybe include the logos of the associations we are members of (North Pinecrest Chamber of Commerce, Federal Guild of Certified Ledgerkeepers, and Continental League of Female Enterprise Founders.

```html
<!DOCTYPE html>
<html lang="en">
<head>
<meta charset="utf-8">
<title>Bright Ledger Accounting – Postcard</title>
<link rel="stylesheet" href="https://fonts.googleapis.com/css2?family=Montserrat:wght@400;500;600;700&family=Source+Serif+4:opsz,wght@8..60,400;8..60,700;8..60,900&family=Tinos:wght@400;700&family=Roboto:wght@700&display=swap">
<style>
:root{
  --navy:#0d3f78;
  --blue:#0054aa;
  --blue-mid:#0677ba;
  --blue-soft:#7badd7;
  --blue-pale:#cadeef;
  --blue-mist:#e8f1f8;
  --teal:#5cc3d6;
  --charcoal:#333436;
  --paper:#f3f3f3;
  --ink:#1c1c1c;
  --page:#e4e4e4;
}
*{margin:0;padding:0;box-sizing:border-box}
html,body{width:881px;height:1200px;overflow:hidden}
body{background:var(--page);position:relative;font-family:"Montserrat",sans-serif}
.card{position:absolute;left:79px;width:723px;height:486px;overflow:hidden;background:#fff}
.card--front{top:84px}
.card--back{top:640px}
.layer{position:absolute;left:0;top:0}

/* front */
.front-logo-band{position:absolute;left:0;top:0;width:723px;height:109px;background:#f1f2f4}
.front-blue{position:absolute;left:0;top:109px;width:723px;height:236px;background:linear-gradient(90deg,#0d4a86,#0b64ab)}
.front-dark{position:absolute;left:0;top:345px;width:723px;height:141px;background:var(--charcoal)}
.brand{position:absolute;display:flex;align-items:center;gap:9px;color:var(--navy);font-family:"Tinos",serif;font-weight:700;line-height:1.05}
.brand__mark{background:var(--navy);display:block;flex:none}
.brand--front{left:43px;top:30px;font-size:25px}
.brand--front .brand__mark{width:26px;height:26px}
.brand--back{left:434px;top:48px;font-size:17px}
.brand--back .brand__mark{width:18px;height:18px}
.headline{position:absolute;left:34px;top:118px;color:#fff;font-family:"Source Serif 4",serif;font-weight:900;line-height:1}
.headline__big{display:block;font-size:53px;letter-spacing:.5px}
.headline__small{display:block;font-size:31px;font-weight:400;margin:-6px 0 -8px 53px}
.tagline{position:absolute;left:36px;top:248px;padding-left:15px;border-left:2px solid #fff;color:#fff;font-size:17.2px;font-weight:500;line-height:20.6px;letter-spacing:.2px}
.contact-line{position:absolute;left:42px;display:flex;align-items:center;gap:8px;color:#fff;font-size:15px;font-weight:500;letter-spacing:.2px}
.contact-line svg{width:18px;height:18px}
.contact-line--email{top:361px}
.contact-line--web{top:387px}
.phone-pill{position:absolute;left:31px;top:420px;width:345px;height:37px;border:1.5px solid #fff;border-radius:19px;display:flex;align-items:center;gap:9px;padding-left:5px;color:#fff;font-weight:700;font-size:20px;letter-spacing:.3px}
.phone-pill__icon{width:27px;height:27px;border-radius:50%;background:#fff;display:flex;align-items:center;justify-content:center}
.phone-pill__sep{font-weight:400;margin:0 3px}

/* back */
.services-tab{position:absolute;left:34px;top:31px;width:189px;height:32px;background:var(--blue-mid);color:#fff;font-size:20px;display:flex;align-items:center;justify-content:center;letter-spacing:.3px}
.services-tab b{font-weight:700;margin-left:6px}
.service{position:absolute;left:34px}
.service__head{display:flex;align-items:flex-end;gap:10px;height:24px}
.service__icon{width:23px;height:23px}
.service__title{color:var(--blue-mid);font-size:13px;font-weight:500;letter-spacing:.3px;padding-bottom:1px;border-bottom:1px solid var(--blue-mid);padding-right:4px}
.service__text{margin-top:9px;font-family:"Tinos",serif;font-size:10px;line-height:11.1px;color:var(--ink)}
.service--books{top:76px}
.service--books .service__title{width:221px}
.service--reports{top:177px}
.service--reports .service__title{width:221px}
.service--payroll{top:267px}
.service--payroll .service__title{width:173px}
.contact-tab{position:absolute;left:34px;top:367px;width:137px;height:26px;background:var(--blue-mid);color:#fff;font-size:12px;font-weight:700;display:flex;align-items:center;justify-content:center;letter-spacing:.4px}
.back-contact{position:absolute;left:40px;display:flex;align-items:center;gap:6px;font-size:10px;color:var(--ink);font-weight:500}
.back-contact svg{width:12px;height:12px}
.back-contact--email{top:404px}
.back-contact--phone{top:422px}
.back-contact--web{top:440px}
.indicia{position:absolute;left:597px;top:40px;width:86px;height:65px;border:1px solid #555;font-family:"Roboto",Arial,sans-serif;font-weight:700;color:#111;text-align:center;padding-top:3px;text-transform:uppercase}
.indicia__line{display:block;font-size:9px;line-height:11px;white-space:nowrap}
.indicia__line--paid{font-size:12px;line-height:14px}
.address-line{position:absolute;left:506px;width:177px;height:1px;background:#222}
</style>
</head>
<body>

<section class="card card--front" aria-label="Postcard front">
  <div class="front-logo-band"></div>
  <div class="front-blue"></div>
  <div class="front-dark"></div>

  <svg class="layer" width="723" height="486" viewBox="0 0 723 486">
    <defs>
      <linearGradient id="photoTone" x1="0" y1="0" x2="1" y2="1">
        <stop offset="0" stop-color="#d9d6d1"/>
        <stop offset=".45" stop-color="#8d8f96"/>
        <stop offset="1" stop-color="#34445e"/>
      </linearGradient>
      <linearGradient id="silverBand" x1="0" y1="0" x2="0" y2="1">
        <stop offset="0" stop-color="#8b8e93"/>
        <stop offset=".5" stop-color="#d6d8db"/>
        <stop offset="1" stop-color="#9a9da2"/>
      </linearGradient>
    </defs>
    <path d="M368,0 C292,118 284,345 440,486 L723,486 L723,0 Z" fill="#0b4f91"/>
    <path d="M396,0 C318,120 312,342 462,486 L723,486 L723,0 Z" fill="url(#silverBand)"/>
    <path d="M408,0 C332,120 326,340 476,486 L723,486 L723,0 Z" fill="url(#photoTone)" role="img" aria-label="Photo of a business team reviewing accounts around a laptop, with a city skyline below"/>
    <path d="M617,300 H687 V362 L652,394 L617,362 Z" fill="#ffffff" role="img" aria-label="LedgerPad CertPartner certification badge"/>
    <circle cx="573" cy="443" r="21" fill="#ffffff" role="img" aria-label="Federal Guild of Certified Ledgerkeepers membership badge"/>
    <circle cx="622" cy="443" r="21" fill="#ffffff" role="img" aria-label="North Pinecrest Chamber of Commerce membership badge"/>
    <circle cx="671" cy="443" r="21" fill="#ffffff" role="img" aria-label="Continental League of Female Enterprise Founders membership badge"/>
  </svg>

  <div class="brand brand--front"><span class="brand__mark"></span><span>Bright Ledger<br>Accounting</span></div>

  <h1 class="headline">
    <span class="headline__big">Accounting</span>
    <span class="headline__small">for your</span>
    <span class="headline__big">Business</span>
  </h1>

  <p class="tagline">Specializing in Cloud-Based<br>Bookkeeping &amp; Payroll<br>Processing with LedgerPad<br>Online by Corvana.</p>

  <div class="contact-line contact-line--email">
    <svg viewBox="0 0 18 18" fill="none" stroke="#fff" stroke-width="1"><circle cx="9" cy="9" r="8.2"/><rect x="4.5" y="6" width="9" height="6.5"/><path d="M4.5 6 L9 9.8 L13.5 6"/></svg>
    Info@BrightLedgerAccounting.com
  </div>
  <div class="contact-line contact-line--web">
    <svg viewBox="0 0 18 18" fill="none" stroke="#fff" stroke-width="1"><circle cx="9" cy="9" r="8.2"/><circle cx="9" cy="9" r="4.5"/><path d="M4.5 9 H13.5 M9 4.5 C7 7 7 11 9 13.5 C11 11 11 7 9 4.5"/></svg>
    www.BrightLedgerAccounting.com
  </div>

  <div class="phone-pill">
    <span class="phone-pill__icon">
      <svg width="16" height="16" viewBox="0 0 24 24" fill="#333436"><path d="M6.6 10.8a15.1 15.1 0 0 0 6.6 6.6l2.2-2.2a1 1 0 0 1 1-.25 11.4 11.4 0 0 0 3.6.57 1 1 0 0 1 1 1V20a1 1 0 0 1-1 1A17 17 0 0 1 3 4a1 1 0 0 1 1-1h3.5a1 1 0 0 1 1 1 11.4 11.4 0 0 0 .57 3.6 1 1 0 0 1-.25 1z"/></svg>
    </span>
    1.800.555.0142<span class="phone-pill__sep">|</span>555.318.2207
  </div>
</section>

<section class="card card--back" aria-label="Postcard back">
  <svg class="layer" width="723" height="486" viewBox="0 0 723 486">
    <rect width="723" height="486" fill="#ffffff"/>
    <path d="M0,0 H322 C470,110 450,370 272,486 H0 Z" fill="var(--blue-mid)"/>
    <path d="M0,0 H306 C450,112 432,372 264,486 H0 Z" fill="var(--navy)"/>
    <path d="M0,0 H268 C385,110 372,365 258,486 H0 Z" fill="#3fa3d4"/>
    <path d="M0,0 H260 C375,110 362,365 252,486 H0 Z" fill="var(--paper)"/>
    <circle cx="428" cy="246" r="23" fill="var(--teal)" opacity=".85"/>
    <circle cx="370" cy="308" r="84" fill="var(--navy)"/>
    <circle cx="370" cy="308" r="79" fill="#c9d3dd" role="img" aria-label="Photo of a laptop showing an accounting dashboard"/>
    <circle cx="309" cy="360" r="21" fill="var(--teal)" opacity=".8"/>
  </svg>

  <div class="services-tab">OUR<b>SERVICES</b></div>

  <article class="service service--books">
    <div class="service__head">
      <svg class="service__icon" viewBox="0 0 24 24" fill="none" stroke="#333" stroke-width="1.1"><rect x="8" y="2" width="13" height="18"/><path d="M11 6h7M11 9h7M11 12h4"/><circle cx="6" cy="16" r="5" fill="#fff"/><path d="M6 13v6M4.5 14.5h2.5a1 1 0 0 1 0 2h-2a1 1 0 0 0 0 2h2.5"/></svg>
      <h2 class="service__title">BOOKKEEPING</h2>
    </div>
    <p class="service__text">Let us take over the day to day bookkeeping so you can get<br>back to running your business. We offer LedgerPad Online<br>setup and ongoing bookkeeping, including daily journal entries,<br>accounts payables &amp; receivables, bill pay, sales tax reporting &amp;<br>payments, account reconciliation, and more.</p>
  </article>

  <article class="service service--reports">
    <div class="service__head">
      <svg class="service__icon" viewBox="0 0 24 24" fill="none" stroke="#333" stroke-width="1.1"><rect x="2" y="2" width="15" height="19"/><path d="M5 17v-3M8 17v-6M11 17v-4"/><circle cx="8" cy="7" r="3"/><circle cx="17" cy="15" r="4" fill="#fff"/><path d="M20 18l3 3"/></svg>
      <h2 class="service__title">FINANCIAL REPORTING</h2>
    </div>
    <p class="service__text">We'll provide easy to understand financial reports that allow<br>you and your team to manage cash flow, create budgets and<br>make forecasting decisions.&nbsp; Want real time data?&nbsp; Let us<br>provide solutions with the latest in mobile apps and dashboards.</p>
  </article>

  <article class="service service--payroll">
    <div class="service__head">
      <svg class="service__icon" viewBox="0 0 24 24" fill="none" stroke="#333" stroke-width="1.1"><path d="M3 2h11l4 4v6"/><path d="M3 2v18h6"/><path d="M6 7h7M6 10h5"/><rect x="10" y="13" width="12" height="9"/><path d="M10 13l6 5 6-5"/></svg>
      <h2 class="service__title">PAYROLL PROCESSING</h2>
    </div>
    <p class="service__text">Whether you have 5 employees or 100+, payroll<br>can be an overwhelming and time consuming task.<br>We offer full service payroll processing, including<br>employee onboarding and reporting.</p>
  </article>

  <div class="contact-tab">CONTACT INFO</div>

  <div class="back-contact back-contact--email">
    <svg viewBox="0 0 12 12" fill="none" stroke="#555" stroke-width=".8"><circle cx="6" cy="6" r="5.5"/><rect x="3" y="4" width="6" height="4.3"/><path d="M3 4l3 2.4L9 4"/></svg>
    info@brightledgeraccounting.com
  </div>
  <div class="back-contact back-contact--phone">
    <svg viewBox="0 0 12 12" fill="none" stroke="#555" stroke-width=".8"><circle cx="6" cy="6" r="5.5"/><path d="M4 3.5l1 1.5-.6.7a4 4 0 0 0 1.9 1.9l.7-.6 1.5 1-.6 1a5 5 0 0 1-4.9-4.9z"/></svg>
    555.318.2207 / 1.800.555.0142
  </div>
  <div class="back-contact back-contact--web">
    <svg viewBox="0 0 12 12" fill="none" stroke="#555" stroke-width=".8"><circle cx="6" cy="6" r="5.5"/><circle cx="6" cy="6" r="3"/><path d="M3 6h6"/></svg>
    www.brightledgeraccounting.com
  </div>

  <div class="brand brand--back"><span class="brand__mark"></span><span>Bright Ledger<br>Accounting</span></div>

  <div class="indicia" aria-label="ZRPX Retail Indicia">
    <span class="indicia__line">PRSRT STD</span>
    <span class="indicia__line">ECRWSS</span>
    <span class="indicia__line">U.S.POSTAGE</span>
    <span class="indicia__line indicia__line--paid">PAID</span>
    <span class="indicia__line">ZRPX RETAIL</span>
  </div>

  <div class="address-line" style="top:269px"></div>
  <div class="address-line" style="top:308px"></div>
  <div class="address-line" style="top:348px"></div>
</section>

</body>
</html>
```